Bluestone Advisory & Mgmt - Professional Business Cards

Hi!

I am a Real Estate Developer and Construction Consultant.

I have a lot of inspiration from previous designs and would be open to using the attached Designs as a starting point. I would like to see these styles incorporated into your designs.

I really need professional business card to go with it that includes my important info.

Look forward to seeing your designs!.

Target Market(s)

My Target market are building owners, lawyers, consultants.

Industry/Entity Type

Real Estate Development

Contact Information for Business Card

My Name: Dorian Pelkey
My Title: Principle
Company Name: Bluestone Advisory & Mgmt, LLC
Address: 348 West 71st Street, 9th FL New York, NY 10010
Mobile: 917.806.3971
Website: bam-hvx.example

Font styles to use
Serif
Sans Serif

Colors

Designer to choose colors to be used in the design.

Requirements
Must have
• Must incorporate the logo attached or have new that looks similar.
• Must use professional font that will be seen and judged by wealthy land owners and developers.
• Must incorporate some of the color green.
Should not have
• Photo's or pictures of people or buildings of any kind.

```html
<!DOCTYPE html>
<html lang="en">
<head>
<meta charset="utf-8">
<title>Bluestone Advisory &amp; Mgmt – Business Cards</title>
<link href="https://fonts.googleapis.com/css2?family=Lato:wght@400;700;900&display=swap" rel="stylesheet">
<style>
  :root {
    --backdrop: #2b2b2c;
    --card: #141314;
    --green: #4dbb7f;
    --stone: #9e9694;
    --muted: #8d8887;
  }
  * { box-sizing: border-box; margin: 0; padding: 0; }
  html, body { width: 1200px; height: 970px; overflow: hidden; }
  body {
    background: var(--backdrop);
    font-family: "Lato", Arial, sans-serif;
    position: relative;
  }
  .card {
    position: absolute;
    width: 700px;
    height: 400px;
    background: var(--card);
    border-bottom: 5px solid var(--green);
    box-shadow: 0 14px 30px rgba(0,0,0,.55);
  }
  .card--front { left: 110px; top: 60px; }
  .card--back { left: 390px; top: 510px; }

  .wordmark {
    position: absolute;
    color: var(--green);
    font-weight: 700;
    line-height: 1.05;
    letter-spacing: .5px;
  }
  .card--front .wordmark { right: 60px; top: 70px; font-size: 40px; text-align: left; }
  .card--back .wordmark { left: 50%; top: 50%; transform: translate(-50%, -50%); font-size: 52px; text-align: left; }
  .wordmark__mark {
    display: inline-block;
    width: 16px; height: 16px;
    background: var(--stone);
    border-radius: 50%;
    margin-right: 10px;
    vertical-align: middle;
  }

  .holder {
    position: absolute;
    left: 0; top: 150px;
    padding-left: 56px;
  }
  .holder__bar {
    position: absolute;
    left: 30px; top: 10px;
    width: 8px; height: 48px;
    background: var(--green);
  }
  .holder__name { color: var(--green); font-weight: 900; font-size: 34px; line-height: 1.1; }
  .holder__title { color: var(--muted); font-size: 16px; margin-top: 2px; }

  .contact {
    position: absolute;
    left: 56px; bottom: 36px;
    color: var(--muted);
    font-size: 16px;
    line-height: 1.35;
  }
  .contact__company { color: var(--green); }
  .contact__lines { list-style: none; margin-top: 6px; }
  .contact__lines li { display: flex; align-items: center; gap: 12px; }
  .contact__icon { width: 16px; height: 16px; flex: none; }
</style>
</head>
<body>

<section class="card card--front" aria-label="Business card front">
  <div class="holder">
    <span class="holder__bar"></span>
    <p class="holder__name">Dorian Pelkey</p>
    <p class="holder__title">Principle</p>
  </div>

  <div class="wordmark"><span class="wordmark__mark"></span>Bluestone<br>Advisory &amp; Mgmt</div>

  <div class="contact">
    <p class="contact__company">Bluestone Advisory &amp; Mgmt, LLC</p>
    <p>348 West 71st Street,</p>
    <p>9th FL New York, NY 10010</p>
    <ul class="contact__lines">
      <li>
        <svg class="contact__icon" viewBox="0 0 16 16"><path d="M3 1.5l3 .5 1 3.5-2 1.2a8 8 0 0 0 4.3 4.3l1.2-2 3.5 1 .5 3c-1 1-2.5 1.5-4 1A12 12 0 0 1 1.5 6C1 4.5 1.5 2.5 3 1.5z" fill="var(--green)"/></svg>
        <span>917.806.3971</span>
      </li>
      <li>
        <svg class="contact__icon" viewBox="0 0 16 16"><rect x="1" y="3" width="14" height="10" fill="var(--green)"/><path d="M1 3l7 6 7-6" fill="none" stroke="var(--card)" stroke-width="1.4"/></svg>
        <span>dorian@bam-hvx.example</span>
      </li>
      <li>
        <svg class="contact__icon" viewBox="0 0 16 16"><circle cx="8" cy="8" r="6.5" fill="none" stroke="var(--green)" stroke-width="1.5"/><path d="M1.5 8h13M8 1.5v13M3 4.5h10M3 11.5h10" stroke="var(--green)" stroke-width="1"/></svg>
        <span>www.bam-hvx.example</span>
      </li>
    </ul>
  </div>
</section>

<section class="card card--back" aria-label="Business card back">
  <div class="wordmark"><span class="wordmark__mark"></span>Bluestone<br>Advisory &amp; Mgmt</div>
</section>

</body>
</html>
```